Eastfield Commercial Card

I would like a modern, eye catching card based off my logo design.
Info to include:
Anders Voll (Card Name)
eastfieldcommercial.example (Website)
555 203 8841 (Office/fax)
555 287 3096 (Business Cell)
anders@eastfieldcommercial.example (Work email)

Target Market(s)

Commercial real estate brokers, property owners.

Colors
ec1f27
757575

Requirements
Must have
• Name and info above. Not be lame!:)

```html
<!DOCTYPE html>
<html lang="en">
<head>
<meta charset="utf-8">
<title>Eastfield Commercial Card</title>
<link rel="stylesheet" href="https://fonts.googleapis.com/css2?family=Arimo:wght@400;700&display=swap">
<style>
  :root {
    --backdrop: #2b2b2b;
    --card-white: #f1f1f1;
    --brand-red: #941b1e;
    --card-red: #9c1c20;
    --card-red-dark: #861619;
    --text-grey: #5a5a5a;
    --white: #ffffff;
  }
  * { box-sizing: border-box; margin: 0; padding: 0; }
  html, body { width: 1200px; height: 960px; overflow: hidden; }
  body {
    background: var(--backdrop);
    font-family: "Arimo", Arial, sans-serif;
    position: relative;
  }
  .card {
    position: absolute;
    width: 600px;
    height: 342px;
  }
  .card-front {
    left: 302px; top: 129px;
    background: linear-gradient(120deg, #f6f6f6 0%, var(--card-white) 60%, #e2e2e2 100%);
  }
  .card-back {
    left: 299px; top: 488px;
    overflow: hidden;
  }
  .brand-mark {
    position: absolute;
    left: 54px; top: 150px;
    width: 240px;
    text-align: center;
    font-weight: 700;
    font-size: 19px;
    color: var(--brand-red);
    text-transform: uppercase;
    letter-spacing: 0.2px;
  }
  .contact {
    position: absolute;
    left: 314px; top: 90px;
    color: var(--text-grey);
    font-size: 14px;
    line-height: 19px;
  }
  .contact-name {
    font-weight: 700;
    font-size: 24px;
    line-height: 28px;
    color: var(--brand-red);
    margin-bottom: 5px;
  }
  .contact-address { margin-bottom: 8px; }
  .contact-list { list-style: none; }
  .contact-list li { display: flex; align-items: center; gap: 7px; }
  .contact-list svg { width: 13px; height: 13px; fill: var(--brand-red); flex: none; }
  .back-surface {
    position: absolute; inset: 0;
    background: linear-gradient(135deg, var(--card-red) 0%, var(--card-red-dark) 100%);
  }
  .back-mark {
    position: absolute;
    left: 0; right: 0; top: 154px;
    text-align: center;
    font-weight: 700;
    font-size: 28px;
    color: var(--white);
    text-transform: uppercase;
    letter-spacing: 0.5px;
  }
</style>
</head>
<body>
  <section class="card card-front">
    <div class="brand-mark">Eastfield Commercial</div>
    <div class="contact">
      <h1 class="contact-name">Anders Voll</h1>
      <p class="contact-address">48 Birchwood lane<br>Harlow MN 55999</p>
      <ul class="contact-list">
        <li><svg viewBox="0 0 16 16"><path d="M3.6 1.2l2.3 2.8-1.3 1.9c.9 2 2.4 3.6 4.5 4.6l1.9-1.3 2.8 2.3-1.3 2.7C7.2 14 2 8.8 1 3.5z"/></svg>555 203 8841</li>
        <li><svg viewBox="0 0 16 16"><path d="M4 0h8a1 1 0 0 1 1 1v14a1 1 0 0 1-1 1H4a1 1 0 0 1-1-1V1a1 1 0 0 1 1-1zm1 2v10h6V2zm3 11a1 1 0 1 0 0 2 1 1 0 0 0 0-2z"/></svg>555 287 3096</li>
        <li><svg viewBox="0 0 16 16"><path d="M1 3h14v10H1zm1.5 1.2L8 8.6l5.5-4.4z"/></svg>anders@eastfieldcommercial.example</li>
        <li><svg viewBox="0 0 16 16"><path d="M8 1a7 7 0 1 0 0 14A7 7 0 0 0 8 1zm0 2c1 1.3 1.6 3 1.7 4.3H6.3C6.4 6 7 4.3 8 3zm-4.8 5.7h1.9c.1 1.5.6 3 1.4 4.1a5.3 5.3 0 0 1-3.3-4.1zm4.8 4.3c-1-1.3-1.6-2.8-1.7-4.3h3.4c-.1 1.5-.7 3-1.7 4.3z"/></svg>www.eastfieldcommercial.example</li>
      </ul>
    </div>
  </section>

  <section class="card card-back">
    <div class="back-surface" role="img" aria-label="Deep red background with a subtle repeating triangle pattern"></div>
    <div class="back-mark">Eastfield Commercial</div>
  </section>
</body>
</html>
```